Master / Title Page for Event Planner Proposal

We design our proposals in Publisher. Attached is our current title page and inside pages. We are looking to update our template to something that is classy yet fun. We plan corporate picnics and holiday parties. Please see attached sample of past proposals. The inside pages need to have a design that is very flexible with the number of images used on the page. The image(s) on the cover page would not change. The cover page can have have many images or just one - whichever is best.

```html
<!DOCTYPE html>
<html lang="en">
<head>
<meta charset="utf-8">
<title>Gala Works – Company Picnic Proposal</title>
<link href="https://fonts.googleapis.com/css2?family=Montserrat:wght@400;500;600;700;800&family=Oswald:wght@500;600&display=swap" rel="stylesheet">
<style>
:root{
  --backdrop:#d3d3d3;
  --navy:#1b3a6e;
  --navy-deep:#13316a;
  --blue:#5b87c9;
  --sky:#dce8f8;
  --ink:#222;
  --grey:#ececec;
  --grey-dark:#a9a9a9;
  --paper:#fff;
}
*{box-sizing:border-box;margin:0;padding:0}
html,body{width:800px;height:1200px;overflow:hidden}
body{background:var(--backdrop);font-family:"Montserrat",sans-serif;color:var(--ink);position:relative}
.page{position:absolute;width:331px;height:468px;background:var(--paper);overflow:hidden;box-shadow:0 1px 3px rgba(0,0,0,.15)}
.photo{position:absolute;border-radius:50%;border:3px solid var(--navy)}
.footer-fade{position:absolute;left:0;right:0;bottom:0;height:60px;background:linear-gradient(to bottom,rgba(255,255,255,0),#c9d8ee 70%,#9fb7dc)}
.site{position:absolute;font-size:6.6px;letter-spacing:.3px;color:var(--ink);font-weight:500}

/* cover */
.cover{left:59px;top:106px}
.cover-header{position:absolute;left:0;top:0;width:100%;height:58px;background:linear-gradient(100deg,#c7dbf5,var(--sky) 45%,#eef4fc);border-bottom:2px solid var(--navy)}
.brand{position:absolute;left:20px;top:18px;font-family:"Montserrat",sans-serif;font-weight:700;font-size:18px;color:var(--navy);letter-spacing:1px;line-height:22px}
.cover-photo{position:absolute;left:0;top:60px;width:100%;height:188px;background:linear-gradient(to bottom,#cfe0ef 0%,#6f9a55 28%,#4f8a36 70%,#3f742b)}
.client{position:absolute;left:0;right:0;top:264px;display:flex;justify-content:center;align-items:center;gap:6px}
.client-dot{width:14px;height:14px;border-radius:50%;background:var(--navy)}
.client-name{font-size:14px;font-weight:600;color:var(--navy);letter-spacing:.6px}
.event-title{position:absolute;left:20px;top:307px;width:142px;text-align:center;font-family:"Oswald",sans-serif;font-weight:600;font-size:16.5px;line-height:19px;color:var(--ink)}
.pill{position:absolute;left:176px;height:11px;background:var(--blue);color:#fff;font-size:7.6px;line-height:11px;padding-left:18px;padding-right:6px}
.pill svg{position:absolute;left:0;top:-1px;width:13px;height:13px}
.pill b{font-weight:500;color:var(--navy-deep)}
.address{position:absolute;left:0;right:0;top:365px;text-align:center;font-size:7.8px}
.slogan{position:absolute;left:0;right:0;top:379px;text-align:center;font-size:8.4px;font-weight:700;letter-spacing:.2px}
.contact{position:absolute;top:404px;height:64px;width:50%;padding:10px 0 0 29px;font-size:6.8px;line-height:9.4px}
.contact.for{left:0;background:#efefef}
.contact.me{right:0;background:var(--blue);color:#fff;padding-left:20px}
.contact .head{font-weight:500}
.contact svg{width:6px;height:6px;vertical-align:-1px;margin-right:4px}

/* commitment */
.commit{left:413px;top:106px;background:linear-gradient(to bottom,#fff 70%,#e3ebf6)}
.commit-band{position:absolute;left:0;top:0;width:100%;height:185px;background:linear-gradient(160deg,#1a3b74,var(--navy-deep) 60%,#0f2a5c)}
.commit-title{position:absolute;left:19px;top:92px;color:#fff;font-weight:800;font-size:21.5px;line-height:22.5px;letter-spacing:.6px}
.commit-rule{position:absolute;left:19px;top:167px;width:82px;height:1.5px;background:#fff}
.lead{position:absolute;left:18px;top:216px;font-size:8.8px;font-weight:700;line-height:9px;color:#1d2a44}
.body{position:absolute;left:19px;width:295px;font-size:6.4px;line-height:7.8px;color:#333}
.subhead{position:absolute;left:19px;top:312px;font-size:9px;font-weight:700;color:#1d2a44}
.end-rule{position:absolute;left:19px;top:449px;width:218px;height:1px;background:#333}

/* menu */
.menu{left:59px;top:619px}
.section-title{position:absolute;left:28px;top:21px;font-size:14.5px;font-weight:700;letter-spacing:.6px;color:var(--ink);border-bottom:1.2px solid var(--ink);line-height:18px}
.section-title span{color:var(--navy)}
.menu-panel{position:absolute;left:18px;top:46px;width:297px;height:393px;background:var(--grey)}
.menu-strip{position:absolute;left:250px;top:420px;width:30px;height:26px;background:var(--grey-dark)}
.intro{position:absolute;left:30px;top:186px;font-size:6.8px}
.intro-strong{position:absolute;left:30px;top:197px;font-size:8.8px;font-weight:700}
.menu-head{position:absolute;left:30px;top:220px;font-size:11px;font-weight:700;text-decoration:underline;text-underline-offset:2px}
.menu-list{position:absolute;left:31px;top:243px;list-style:none;font-size:6.6px;line-height:8.45px;color:#222}
.menu-list li{display:flex;align-items:center;gap:3px}
.menu-list svg{width:6px;height:6px}
.menu-list .strong{font-weight:700;font-size:7.8px;line-height:10px}
.price-tag{position:absolute;left:32px;top:425px;width:74px;height:18px;background:var(--grey-dark);color:var(--navy);font-size:8.4px;font-weight:700;text-align:center;line-height:18px;box-shadow:0 1px 1px rgba(0,0,0,.2)}

/* dj */
.dj{left:413px;top:619px;background:#fff}
.dj-text-head{position:absolute;left:21px;top:231px;font-size:8.8px;font-weight:700;color:#1d2a44}
.dj .body{left:21px;width:290px}
.dj .note{position:absolute;left:21px;font-size:6.6px;font-weight:600;color:#222}
.best{position:absolute;left:217px;top:293px;width:75px;height:18px;background:var(--grey-dark);color:#333;text-align:center;font-size:9px;font-weight:600;line-height:18px}
.best-price{position:absolute;left:227px;top:312px;width:56px;height:15px;background:var(--navy);color:#fff;text-align:center;font-size:7.6px;font-weight:700;line-height:15px}
</style>
</head>
<body>
<svg width="0" height="0" style="position:absolute" aria-hidden="true">
  <symbol id="tick" viewBox="0 0 12 12"><circle cx="6" cy="6" r="5" fill="none" stroke="#1b3a6e" stroke-width="1.2"/><path d="M3.4 6.2 5.3 8 8.8 4.2" fill="none" stroke="#1b3a6e" stroke-width="1.3"/></symbol>
  <symbol id="phone" viewBox="0 0 12 12"><path d="M1 4c0-2 2-3 5-3s5 1 5 3l-2 1-1-1.5H4L3 5zM3 6h6l1.5 5h-9z" fill="currentColor"/></symbol>
  <symbol id="mail" viewBox="0 0 12 12"><rect x="1" y="2.5" width="10" height="7" fill="currentColor"/><path d="M1 2.5 6 7l5-4.5" fill="none" stroke="#fff" stroke-width=".9"/></symbol>
</svg>

<section class="page cover">
  <div class="cover-header">
    <div class="brand">Gala Works</div>
  </div>
  <div class="cover-photo" role="img" aria-label="Aerial photo of a large company picnic on a lawn with inflatables and tents"></div>
  <div class="client"><span class="client-dot"></span><span class="client-name">HARROW BIOSCIENCES</span></div>
  <h1 class="event-title">Company Picnic<br>2020- Event Estimate</h1>
  <div class="pill" style="top:305px"><svg viewBox="0 0 13 13"><circle cx="6.5" cy="6.5" r="6.5" fill="#13316a"/><rect x="3.5" y="4" width="6" height="5" fill="none" stroke="#fff" stroke-width=".9"/></svg>Sunday, April 19, 2020</div>
  <div class="pill" style="top:322px"><svg viewBox="0 0 13 13"><circle cx="6.5" cy="6.5" r="6.5" fill="#13316a"/><circle cx="6.5" cy="6.5" r="3" fill="none" stroke="#fff" stroke-width=".9"/><path d="M6.5 5v1.7h1.3" stroke="#fff" stroke-width=".8" fill="none"/></svg>12:00 - 3:00 PM</div>
  <div class="pill" style="top:339px"><svg viewBox="0 0 13 13"><circle cx="6.5" cy="6.5" r="6.5" fill="#13316a"/><path d="M6.5 10 4.3 6.4a2.4 2.4 0 1 1 4.4 0z" fill="none" stroke="#fff" stroke-width=".9"/></svg>On Site: <b>galaworks.com</b></div>
  <p class="address">Address here more address here Based on 200 guests</p>
  <p class="slogan">Whatever the Event...We are the Solution!</p>
  <div class="contact for">
    <div class="head">This proposal prepared for:</div>
    <div>Client Name</div>
    <div><svg><use href="#phone"/></svg>555.201.3390</div>
    <div><svg><use href="#mail"/></svg>client@harrowbio.com</div>
  </div>
  <div class="contact me">
    <div class="head">Contact me with any questions:</div>
    <div>Dana Whitfield</div>
    <div><svg><use href="#phone"/></svg>555.204.7712</div>
    <div><svg><use href="#mail"/></svg>dana@galaworks.com</div>
  </div>
</section>

<section class="page commit">
  <div class="commit-band"></div>
  <h2 class="commit-title">OUR COMMITMENT<br>AND SERVICE<br>TO YOU!</h2>
  <div class="commit-rule"></div>
  <p class="lead">Gala Works takes pride in providing<br>superior quality service!</p>
  <p class="body" style="top:242px">You are our guests and we take that responsibility seriously. All Gala Works’ team members are service-oriented, conscientious professionals. You can expect friendly smiles, positive communication and a staff who is happy and honored to serve you!</p>
  <p class="body" style="top:274px">We carefully plan and customize corporate events with attention to every detail. We value professionalism and we make you our top priority.</p>
  <h3 class="subhead">What to Expect</h3>
  <p class="body" style="top:329px">Assistance booking suppliers, vendors and services on and off site. Full coordination of your event from the first inquiry to the final departure.</p>
  <p class="body" style="top:349px">Unlimited communication throughout the planning process.</p>
  <div class="end-rule"></div>
  <span class="site" style="left:241px;top:445px">galaworks.com</span>
</section>

<section class="page menu">
  <div class="footer-fade"></div>
  <h2 class="section-title">THE <span>TRADITIONAL MENU</span></h2>
  <div class="menu-panel"></div>
  <div class="menu-strip"></div>
  <div class="photo" style="left:12px;top:56px;width:110px;height:110px;background:radial-gradient(#b5552a,#2a1c18)" role="img" aria-label="Hot dogs on a grill"></div>
  <div class="photo" style="left:109px;top:56px;width:110px;height:110px;background:radial-gradient(#e8e8e8,#8a7a72)" role="img" aria-label="Burgers cooking on a smoky grill"></div>
  <div class="photo" style="left:207px;top:56px;width:110px;height:110px;background:radial-gradient(#6b4a35,#2a1a12 70%,#d9711d)" role="img" aria-label="Burger patty over flames"></div>
  <p class="intro">Cooked On-Site On Beautiful State-Of-The-Art Grills Seasoned With Oak Wood</p>
  <p class="intro-strong">Served from Multiple Buffets to Avoid Lines!</p>
  <h3 class="menu-head">Menu</h3>
  <ul class="menu-list">
    <li><svg><use href="#tick"/></svg>Mouth Watering Quarter Pound</li>
    <li><svg><use href="#tick"/></svg>Charbroiled Hamburgers</li>
    <li><svg><use href="#tick"/></svg>Cheeseburgers Harlan’s All Beef Hot Dogs</li>
    <li class="strong"><svg><use href="#tick"/></svg>Veggie Burgers Available upon Request</li>
    <li><svg><use href="#tick"/></svg>Old Fashioned Potato Salad</li>
    <li><svg><use href="#tick"/></svg>Creamy Cole Slaw</li>
    <li><svg><use href="#tick"/></svg>Assorted Fresh Baked Cookies</li>
    <li><svg><use href="#tick"/></svg>Iced Water</li>
    <li><svg><use href="#tick"/></svg>Fruit Punch</li>
    <li><svg><use href="#tick"/></svg>Lemonade and Iced Tea</li>
    <li><svg><use href="#tick"/></svg>Yellow Mustard</li>
    <li><svg><use href="#tick"/></svg>Ketchup</li>
    <li><svg><use href="#tick"/></svg>Relish</li>
    <li><svg><use href="#tick"/></svg>Onions</li>
    <li><svg><use href="#tick"/></svg>Mayonnaise</li>
    <li><svg><use href="#tick"/></svg>Pickles</li>
    <li><svg><use href="#tick"/></svg>Lettuce and Tomatoes</li>
    <li><svg><use href="#tick"/></svg>Disposable Plates</li>
    <li><svg><use href="#tick"/></svg>Cups and Napkin Packs</li>
  </ul>
  <div class="photo" style="left:229px;top:207px;width:70px;height:70px;background:radial-gradient(#b78350,#4a2c1a)" role="img" aria-label="Assorted cookies"></div>
  <div class="photo" style="left:229px;top:282px;width:70px;height:70px;background:radial-gradient(#f4eed0,#c9c196 70%,#6c9a3a)" role="img" aria-label="Potato salad"></div>
  <div class="photo" style="left:229px;top:357px;width:70px;height:70px;background:radial-gradient(#f3f1e6,#d8d3b8 70%,#b9b39a)" role="img" aria-label="Cole slaw"></div>
  <div class="price-tag">$13,295.00</div>
  <span class="site" style="left:239px;top:453px">galaworks.com</span>
</section>

<section class="page dj">
  <div class="footer-fade"></div>
  <h2 class="section-title" style="left:20px">DJ, BINGO AND PRIZES</h2>
  <div class="photo" style="left:57px;top:70px;width:142px;height:142px;background:linear-gradient(to bottom,#8fae6a,#6aa34a 40%,#c98a70)" role="img" aria-label="Guests browsing a prize table outdoors"></div>
  <div class="photo" style="left:181px;top:39px;width:154px;height:154px;background:radial-gradient(#9b8a70,#4d5560)" role="img" aria-label="Guests playing bingo at a long table"></div>
  <h3 class="dj-text-head">DJ, BINGO and Prizes</h3>
  <p class="body" style="top:247px">Your event will be staffed with a professional DJ who will host fun games of BINGO, dance contests and family friendly music throughout your event.</p>
  <p class="note" style="top:266px">Large and small quality prizes will be awarded approximately every 20 minutes.</p>
  <p class="note" style="top:275px"><b>Prizes may include:</b> <span style="font-weight:500">Burger Barn, Pasta House gift cards, Blenders, Toys</span></p>
  <p class="note" style="top:288px;font-size:7.8px;font-weight:700">You can expect high energy and lots of fun!</p>
  <div class="best">Best Price</div>
  <div class="best-price">$12,295.00</div>
  <div class="photo" style="left:35px;top:341px;width:80px;height:80px;background:radial-gradient(#7a8aa0,#2c3240)" role="img" aria-label="DJ crew at an outdoor event"></div>
  <div class="photo" style="left:125px;top:341px;width:80px;height:80px;background:radial-gradient(#8a7060,#3a2e28)" role="img" aria-label="Hands marking bingo cards"></div>
  <div class="photo" style="left:215px;top:341px;width:80px;height:80px;background:radial-gradient(#e6b87a,#3a5a8a)" role="img" aria-label="Holding a bingo card"></div>
  <span class="site" style="left:239px;top:447px">galaworks.com</span>
</section>
</body>
</html>
```